Business Card Design needed for logo design project

Our company needs a Business Card Design. Please refer to our original project in the link above.
Dorian Pellworth
Broker

W: Velvetcrestestates.example
P: 555-302-7184
F: 555-741-2096
E: dorianpellworth@mailbox.example
A: North Dallas Office
Updates

Name Spelling update , sorry Dorian Pellworth card is double sided

```html
<!DOCTYPE html>
<html lang="en">
<head>
<meta charset="utf-8">
<title>Velvetcrest Estates – Business Card Options</title>
<link rel="stylesheet" href="https://fonts.googleapis.com/css2?family=Cinzel:wght@400;600&display=swap">
<style>
  :root {
    --charcoal: #444243;
    --green: #00a651;
    --gold: #a88650;
    --gold-text: #a8804a;
    --white: #ffffff;
    --sheet: #ffffff;
  }
  html, body {
    margin: 0;
    padding: 0;
    width: 1050px;
    height: 1200px;
    overflow: hidden;
    background: var(--sheet);
  }
  .sheet {
    position: relative;
    width: 1050px;
    height: 1200px;
  }
  .card {
    position: absolute;
    width: 338px;
    height: 593px;
    overflow: hidden;
    font-family: "Cinzel", "Times New Roman", serif;
  }
  .card--col1 { left: 6px; }
  .card--col2 { left: 356px; }
  .card--col3 { left: 706px; }
  .card--row1 { top: 4px; }
  .card--row2 { top: 603px; }

  .brand-area {
    position: absolute;
    left: 0;
    top: 0;
    width: 100%;
    height: 427px;
    display: flex;
    flex-direction: column;
    align-items: center;
    justify-content: center;
    gap: 26px;
  }
  .brand-area--dark { background: var(--charcoal); }
  .brand-area--light { background: var(--white); }

  .brand-mark {
    width: 120px;
    height: 120px;
    border-radius: 50%;
    background: var(--gold);
  }
  .brand-name {
    margin: 0;
    text-align: center;
    color: var(--gold-text);
    font-weight: 400;
    font-size: 27px;
    line-height: 1.15;
    letter-spacing: 0.5px;
  }

  .divider {
    position: absolute;
    left: 0;
    top: 427px;
    width: 100%;
    height: 4px;
  }
  .divider--gold { background: var(--gold); }
  .divider--green { background: var(--green); }

  .contact-panel {
    position: absolute;
    left: 0;
    bottom: 0;
    width: 100%;
    height: 162px;
    color: var(--white);
    text-align: center;
    padding-top: 16px;
    box-sizing: border-box;
  }
  .contact-panel--green { background: var(--green); }
  .contact-panel--gold { background: var(--gold); }

  .contact-name {
    margin: 0;
    font-size: 13.5px;
    font-weight: 600;
    letter-spacing: 0.4px;
  }
  .contact-title {
    margin: 5px 0 0;
    font-size: 8px;
    letter-spacing: 0.5px;
  }
  .contact-list {
    list-style: none;
    margin: 21px 0 0;
    padding: 0;
    font-size: 10.5px;
    line-height: 19px;
    letter-spacing: 0.2px;
  }
</style>
</head>
<body>
<main class="sheet">

  <!-- Row 1 -->
  <article class="card card--row1 card--col1">
    <header class="brand-area brand-area--dark">
      <span class="brand-mark"></span>
      <h1 class="brand-name">VELVETCREST<br>ESTATES</h1>
    </header>
    <div class="divider divider--gold"></div>
    <section class="contact-panel contact-panel--green">
      <p class="contact-name">DORIAN PELLWORTH</p>
      <p class="contact-title">BROKER</p>
      <ul class="contact-list">
        <li>P: 555-302-7184</li>
        <li>F: 555-741-2096</li>
        <li>W: VELVETCRESTESTATES.EXAMPLE</li>
        <li>E: DORIANPELLWORTH@MAILBOX.EXAMPLE</li>
      </ul>
    </section>
  </article>

  <article class="card card--row1 card--col2">
    <header class="brand-area brand-area--dark">
      <span class="brand-mark"></span>
      <h1 class="brand-name">VELVETCREST<br>ESTATES</h1>
    </header>
    <section class="contact-panel contact-panel--green">
      <p class="contact-name">DORIAN PELLWORTH</p>
      <p class="contact-title">BROKER</p>
      <ul class="contact-list">
        <li>P: 555-302-7184</li>
        <li>F: 555-741-2096</li>
        <li>W: VELVETCRESTESTATES.EXAMPLE</li>
        <li>E: DORIANPELLWORTH@MAILBOX.EXAMPLE</li>
      </ul>
    </section>
  </article>

  <article class="card card--row1 card--col3">
    <header class="brand-area brand-area--light">
      <span class="brand-mark"></span>
      <h1 class="brand-name">VELVETCREST<br>ESTATES</h1>
    </header>
    <section class="contact-panel contact-panel--green">
      <p class="contact-name">DORIAN PELLWORTH</p>
      <p class="contact-title">BROKER</p>
      <ul class="contact-list">
        <li>P: 555-302-7184</li>
        <li>F: 555-741-2096</li>
        <li>W: VELVETCRESTESTATES.EXAMPLE</li>
        <li>E: DORIANPELLWORTH@MAILBOX.EXAMPLE</li>
      </ul>
    </section>
  </article>

  <!-- Row 2 -->
  <article class="card card--row2 card--col1">
    <header class="brand-area brand-area--dark">
      <span class="brand-mark"></span>
      <h1 class="brand-name">VELVETCREST<br>ESTATES</h1>
    </header>
    <div class="divider divider--green"></div>
    <section class="contact-panel contact-panel--gold">
      <p class="contact-name">DORIAN PELLWORTH</p>
      <p class="contact-title">BROKER</p>
      <ul class="contact-list">
        <li>P: 555-302-7184</li>
        <li>F: 555-741-2096</li>
        <li>W: VELVETCRESTESTATES.EXAMPLE</li>
        <li>E: DORIANPELLWORTH@MAILBOX.EXAMPLE</li>
      </ul>
    </section>
  </article>

  <article class="card card--row2 card--col2">
    <header class="brand-area brand-area--dark">
      <span class="brand-mark"></span>
      <h1 class="brand-name">VELVETCREST<br>ESTATES</h1>
    </header>
    <section class="contact-panel contact-panel--gold">
      <p class="contact-name">DORIAN PELLWORTH</p>
      <p class="contact-title">BROKER</p>
      <ul class="contact-list">
        <li>P: 555-302-7184</li>
        <li>F: 555-741-2096</li>
        <li>W: VELVETCRESTESTATES.EXAMPLE</li>
        <li>E: DORIANPELLWORTH@MAILBOX.EXAMPLE</li>
      </ul>
    </section>
  </article>

  <article class="card card--row2 card--col3">
    <header class="brand-area brand-area--light">
      <span class="brand-mark"></span>
      <h1 class="brand-name">VELVETCREST<br>ESTATES</h1>
    </header>
    <section class="contact-panel contact-panel--gold">
      <p class="contact-name">DORIAN PELLWORTH</p>
      <p class="contact-title">BROKER</p>
      <ul class="contact-list">
        <li>P: 555-302-7184</li>
        <li>F: 555-741-2096</li>
        <li>W: VELVETCRESTESTATES.EXAMPLE</li>
        <li>E: DORIANPELLWORTH@MAILBOX.EXAMPLE</li>
      </ul>
    </section>
  </article>

</main>
</body>
</html>
```